Tolvik Waste Website Design

Our new start-up needs a website design. We plan to help businesses find more sustainable ways to manage their waste. Our initial website aims to gather contact data from potential business customers and comprehensive information from waste facilities and waste transporters. We have a logo design (attached) which we would like included in the website design. I have also attached a number of pages that describe what information should appear on each page as well as a web design brief file that describes the look we are after.

```html
<!DOCTYPE html>
<html lang="en">
<head>
<meta charset="utf-8">
<title>Tolvik Waste</title>
<link href="https://fonts.googleapis.com/css2?family=Titillium+Web:wght@400;600;700&family=Lato:wght@300;400;700&display=swap" rel="stylesheet">
<style>
:root{
  --green-dark:#325a28;
  --green-brand:#8cc63f;
  --ink:#333333;
  --muted:#666666;
  --panel:#f4f4f4;
  --line:#e6e6e6;
  --yellow:#f3d42e;
  --link-green:#3d7a28;
}
*{margin:0;padding:0;box-sizing:border-box}
html,body{width:1200px;height:993px;overflow:hidden;background:#fff}
body{position:relative;font-family:"Lato",sans-serif;color:var(--ink)}
.abs{position:absolute}

.site-header{left:0;top:0;width:1200px;height:89px;background:#fff}
.brand{left:8px;top:14px;display:flex;align-items:center;gap:10px}
.brand-mark{width:56px;height:56px;border-radius:50%;background:var(--green-brand)}
.brand-name{font-family:"Titillium Web",sans-serif;font-weight:600;font-size:30px;color:#4a4a4a;letter-spacing:1px}
.main-nav{top:33px;font-family:"Titillium Web",sans-serif;font-weight:600;font-size:13px;color:var(--ink)}

.hero{left:0;top:89px;width:1200px;height:251px;
  background:radial-gradient(ellipse at 75% 60%,#5b9a1e 0%,#4f8c18 35%,#7cbc2e 75%,#92c940 100%)}
.hero-title,.hero-sub{width:1200px;text-align:center;color:#fff;font-family:"Titillium Web",sans-serif;font-weight:600;text-shadow:0 1px 3px rgba(0,0,0,.35)}
.hero-title{top:118px;font-size:23px}
.hero-sub{top:168px;font-size:19px}

.services-band{left:0;top:340px;width:1200px;height:376px;background:var(--panel)}
.service-card{top:348px;width:374px;height:214px;background:#fff;box-shadow:0 1px 2px rgba(0,0,0,.06);text-align:center}
.service-card svg{position:absolute;left:50%;transform:translateX(-50%);top:6px}
.service-card h3{position:absolute;left:0;right:0;top:174px;font-family:"Titillium Web",sans-serif;font-weight:600;font-size:16px;color:var(--ink)}

.signup{left:126px;top:590px;width:948px;height:94px;background:#fff;box-shadow:0 1px 2px rgba(0,0,0,.05)}
.signup-input{left:25px;top:25px;width:539px;height:33px;border:1px solid #e2e2e2;font-size:10px;color:#666;padding:10px 9px;font-family:"Lato",sans-serif}
.signup-button{left:610px;top:25px;width:270px;height:32px;background:var(--yellow);color:var(--link-green);font-weight:700;font-size:10.5px;text-align:center;line-height:32px}

.map-area{left:0;top:741px;width:361px;height:158px;background:linear-gradient(135deg,#eceae4,#e2e4e0)}

.footer-links{left:398px;top:741px;width:360px;list-style:none}
.footer-links li{height:23.2px;border-bottom:1px solid var(--line);text-align:center;font-size:9.6px;color:var(--link-green);line-height:23px}

.contact-title{left:840px;top:741px;font-family:"Titillium Web",sans-serif;font-weight:600;font-size:10px;color:var(--ink)}
.contact-rule{left:840px;top:766px;width:360px;height:1px;background:var(--line)}
.contact-lines{left:840px;font-size:9.6px;color:var(--muted);line-height:16.4px;font-weight:300}

.footer-rule{left:0;top:929px;width:1200px;height:1px;background:var(--line)}
.copyright{left:0;top:956px;width:1200px;text-align:center;font-size:7.5px;letter-spacing:.6px;color:#999}
</style>
</head>
<body>

<header class="abs site-header">
  <div class="abs brand">
    <span class="brand-mark"></span>
    <span class="brand-name">Tolvik Waste</span>
  </div>
  <nav>
    <span class="abs main-nav" style="left:852px">About Us</span>
    <span class="abs main-nav" style="left:933px">What We Do</span>
    <span class="abs main-nav" style="left:1032px">Resources</span>
    <span class="abs main-nav" style="left:1120px">Contact Us</span>
  </nav>
</header>

<section class="abs hero" role="img" aria-label="Close-up photograph of a textured green leaf"></section>
<h1 class="abs hero-title">Welcome to Tolvik Waste</h1>
<p class="abs hero-sub">Take Control of Your Waste Here &amp; Make a Difference!</p>

<div class="abs services-band"></div>

<article class="abs service-card" style="left:7px">
  <svg width="146" height="152" viewBox="0 0 146 152">
    <path fill="#325a28" d="M38 0h69v88h30v64H0V64h38z"/>
    <g fill="#fff">
      <rect x="51" y="13" width="12" height="12"/><rect x="82" y="13" width="12" height="12"/>
      <rect x="51" y="38" width="12" height="12"/><rect x="82" y="38" width="12" height="12"/>
      <rect x="13" y="63" width="12" height="12"/><rect x="51" y="63" width="12" height="12"/><rect x="82" y="63" width="12" height="12"/>
      <rect x="13" y="88" width="12" height="12"/><rect x="51" y="88" width="12" height="12"/><rect x="82" y="88" width="12" height="12"/><rect x="118" y="88" width="12" height="12"/>
      <rect x="13" y="114" width="12" height="25"/><rect x="51" y="114" width="18" height="25"/><rect x="75" y="114" width="19" height="25"/><rect x="118" y="114" width="12" height="25"/>
    </g>
  </svg>
  <h3>Waste Facilities</h3>
</article>

<article class="abs service-card" style="left:413px">
  <svg width="128" height="152" viewBox="0 0 128 152">
    <path fill="#325a28" d="M46 0h36v12h46v12H0V12h46zM6 38h114v114H6z"/>
    <g fill="#fff"><rect x="26" y="57" width="12" height="76" rx="6"/><rect x="57" y="57" width="12" height="76" rx="6"/><rect x="88" y="57" width="12" height="76" rx="6"/></g>
  </svg>
  <h3>Waste Producer</h3>
</article>

<article class="abs service-card" style="left:819px">
  <svg width="154" height="150" viewBox="0 0 154 150">
    <path fill="#325a28" d="M0 34l38-28 14 22h84l16 30 0 52-8 8H20L12 90zM96 22h20l2 12H96z"/>
    <path fill="#325a28" d="M6 34h94l-10 62H18z"/>
    <circle cx="45" cy="115" r="26" fill="#325a28"/><circle cx="117" cy="115" r="26" fill="#325a28"/>
    <circle cx="45" cy="115" r="10" fill="#fff"/><circle cx="117" cy="115" r="10" fill="#fff"/>
    <rect x="104" y="40" width="26" height="20" fill="#fff"/>
    <g fill="#fff"><path d="M25 55h6l4 28h-6z"/><path d="M38 55h6l4 28h-6z"/><path d="M51 55h6l4 28h-6z"/></g>
  </svg>
  <h3>Waste Transporter</h3>
</article>

<form class="abs signup">
  <div class="abs signup-input">E-Mail Address</div>
  <div class="abs signup-button">Register NOW!</div>
</form>

<div class="abs map-area" role="img" aria-label="Street map showing the office location"></div>

<ul class="abs footer-links">
  <li>About Us</li><li>What we do</li><li>Resources</li><li>Contact Us</li>
  <li>Waste Facilities</li><li>Waste Producer</li><li>Waste Transporter</li>
</ul>

<div class="abs contact-title">Contact Us</div>
<div class="abs contact-rule"></div>
<div class="abs contact-lines" style="top:780px">
  Street: 18 Larkin Road<br>City: Fernleigh<br>State: New South Wales<br>Country: Australia
</div>
<div class="abs contact-lines" style="top:860px">
  Phone: (02) 5550 1847<br>Email: hello@tolvikwaste.com
</div>

<div class="abs footer-rule"></div>
<p class="abs copyright">COPYRIGHT © 2018 · MERIDIAN THEME ON NORTHGATE FRAMEWORK · SITECRAFT · LOG OUT</p>

</body>
</html>
```